Adventurous female pilot

I am looking for a personal business card, for a very well qualified female pilot, with a lot of aviation experience.

Currently an airline pilot, have worked as a bush pilot in Africa, looking to get into corporate aviation, or private jet owners.
Want a classy looking card for networking...

Could be interested in a retro\vintage look also?!

An idea,, is an african sunset background, with my wings\logo on it
Updates

I just want to say thank you to all of your for your amazing designs!

I have been very busy flying this past week , so not had a chance to be on the computer much.
But I provide some feedback, and conclusions very soon!
Thank you again.

Maren

Reason: Still waiting on a couple of revisions to be 100% about my choice!

Target Market(s)

corporate aviation, private jet owners, casino's,
General audience.
networking

Industry/Entity Type

Airline

Requirements
Nice to have
• Classy, edgy, sexy, but also feminine

```html
<!DOCTYPE html>
<html lang="en">
<head>
<meta charset="utf-8">
<title>Maren Hollis – Business Card</title>
<link rel="stylesheet" href="https://fonts.googleapis.com/css2?family=Questrial&display=swap">
<style>
  :root {
    --page-bg: #ece8e1;
    --sky-top: #5e1405;
    --sky-mid: #a9400a;
    --sky-low: #dc7d10;
    --sun: #f7b51e;
    --sun-glow: rgba(250, 190, 40, 0.55);
    --savanna-dark: #2a1305;
    --savanna-mid: #7a3f0c;
    --grass: #e09a1e;
    --grass-light: #f0b53a;
    --text-light: #ffffff;
    --text-dark: #1c0f05;
  }
  * { margin: 0; padding: 0; box-sizing: border-box; }
  html, body {
    width: 1200px;
    height: 1000px;
    overflow: hidden;
    background: var(--page-bg);
    font-family: "Questrial", "Century Gothic", sans-serif;
  }
  .card {
    position: absolute;
    left: 100px;
    top: 215px;
    width: 1000px;
    height: 570px;
    border-radius: 10px 130px 10px 10px;
    overflow: hidden;
    background: linear-gradient(180deg, var(--sky-top) 0%, var(--sky-mid) 30%, var(--sky-low) 62%, var(--grass) 100%);
  }
  .sun {
    position: absolute;
    left: 320px;
    top: -40px;
    width: 380px;
    height: 380px;
    border-radius: 50%;
    background: radial-gradient(circle, var(--sun) 0%, var(--sun) 48%, var(--sun-glow) 62%, rgba(247,181,30,0) 72%);
  }
  .aircraft-art {
    position: absolute;
    left: 370px;
    top: 55px;
    width: 300px;
    height: 85px;
    border-radius: 6px;
    background: linear-gradient(180deg, rgba(60,30,5,0.28), rgba(60,30,5,0.12));
  }
  .brand {
    position: absolute;
    left: 260px;
    top: 205px;
    width: 500px;
    text-align: center;
    color: var(--text-dark);
    font-size: 46px;
    letter-spacing: 6px;
    line-height: 1;
  }
  .savanna-art {
    position: absolute;
    left: 0;
    top: 330px;
    width: 1000px;
    height: 140px;
    background: linear-gradient(180deg, rgba(42,19,5,0.0) 0%, rgba(42,19,5,0.55) 35%, var(--savanna-dark) 70%, var(--savanna-mid) 100%);
  }
  .grass-band {
    position: absolute;
    left: 0;
    bottom: 0;
    width: 1000px;
    height: 100px;
    background: linear-gradient(180deg, var(--grass-light), var(--grass));
  }
  .name {
    position: absolute;
    right: 32px;
    top: 378px;
    color: var(--text-light);
    font-size: 42px;
  }
  .email {
    position: absolute;
    right: 32px;
    top: 430px;
    color: var(--text-light);
    font-size: 29px;
  }
  .phone {
    position: absolute;
    color: var(--text-dark);
    font-size: 29px;
  }
  .phone-us { left: 28px; top: 484px; }
  .phone-taipei { right: 32px; top: 522px; }
</style>
</head>
<body>
  <div class="card">
    <div class="sun"></div>
    <div class="aircraft-art" role="img" aria-label="Three vintage biplane silhouettes flying across the sun"></div>
    <div class="brand">SKYROVE</div>
    <div class="savanna-art" role="img" aria-label="African savanna silhouettes: acacia trees, elephant and giraffes at sunset"></div>
    <div class="grass-band"></div>
    <div class="name">Maren Hollis</div>
    <div class="email">Email: marenhollis@skyrovemail.com</div>
    <div class="phone phone-us">Cell US: +1 702-555-0147</div>
    <div class="phone phone-taipei">Cell Taipei: +886 970-555-268</div>
  </div>
</body>
</html>
```